Business card design needed

We need a new business card design for a new company based in Melbourne Australia called Tallo Ventures.
We develop new products and are about to launch our first product into the health and hygiene market.
We would like our business card to be targeted at corporate/business.
We would like to see designs that use the colours blue and white and incorporate our company name logo (attached).
We would like double sided.
We would also like an infinity symbol incorporated into the design in an unusual way (eg stretched or out of proportion).
The final design should communicate innovation.

Industry/Entity Type

Health

Contact Information for Business Card

Business Name
Name
Position
Address line 1
Address line 2
Telephone 1
Telephone 2
Email
Website

Requirements
Must have
• Company name logo (attached)
Infinity symbol incorporated into design

```html
<!DOCTYPE html>
<html lang="en">
<head>
<meta charset="utf-8">
<title>Tallo Ventures – Business Card</title>
<link rel="stylesheet" href="https://fonts.googleapis.com/css2?family=Fira+Sans:wght@400;500;600&display=swap">
<style>
  :root {
    --board: #d4e4e5;
    --card: #ffffff;
    --stripe-tone: #c6def5;
    --stripe-pale: #e6f0fa;
    --ink: #1f45d8;
    --brand: #1a52e6;
    --shadow: rgba(60, 100, 170, 0.55);
    --rule: #ffffff;
  }
  * { margin: 0; padding: 0; box-sizing: border-box; }
  html, body { width: 849px; height: 1200px; overflow: hidden; }
  body {
    position: relative;
    background: var(--board);
    font-family: "Fira Sans", "Helvetica Neue", Arial, sans-serif;
  }
  .card {
    position: absolute;
    left: 186px;
    width: 475px;
    height: 275px;
    background: var(--card);
    box-shadow: 0 3px 10px var(--shadow);
    overflow: hidden;
  }
  .card--front { top: 179px; }
  .card--back { top: 511px; }
  .card__backdrop { position: absolute; inset: 0; width: 100%; height: 100%; }
  .wordmark {
    position: absolute;
    color: var(--brand);
    font-weight: 500;
    font-size: 28px;
    line-height: 1;
    white-space: nowrap;
  }
  .card--front .wordmark { left: 24px; top: 46px; }
  .card--back .wordmark { left: 44px; top: 39px; }
  .contact {
    position: absolute;
    left: 45px;
    top: 106px;
    color: var(--ink);
    font-size: 15px;
    line-height: 1;
    letter-spacing: 0.9px;
  }
  .contact__business { font-size: 16.5px; font-weight: 600; letter-spacing: 0.6px; }
  .contact__name { font-size: 15px; font-weight: 600; margin-top: 3px; }
  .contact__position { margin-top: 7px; }
  .contact__address { margin-top: 6px; }
  .contact__phones, .contact__web { margin-top: 6px; }
  .sep { margin: 0 6px; }
  .board-rule {
    position: absolute;
    left: 0; right: 0;
    top: 1106px;
    height: 3px;
    background: var(--rule);
  }
  .board-mark {
    position: absolute;
    right: 48px;
    top: 1118px;
    color: var(--rule);
    font-size: 18px;
    font-weight: 500;
  }
</style>
</head>
<body>
  <section class="card card--front" aria-label="Business card front">
    <svg class="card__backdrop" viewBox="0 0 475 275" role="img" aria-label="Light blue diagonal stripe texture cut by a sweeping white arc band">
      <rect width="475" height="275" fill="var(--stripe-tone)"/>
      <path fill="var(--card)" fill-rule="evenodd"
        d="M-250 330 a362 320 0 1 0 724 0 a362 320 0 1 0 -724 0 Z
           M-215 330 a325 225 0 1 0 650 0 a325 225 0 1 0 -650 0 Z"/>
    </svg>
    <div class="wordmark">Tallo Ventures</div>
  </section>

  <section class="card card--back" aria-label="Business card back">
    <svg class="card__backdrop" viewBox="0 0 475 275" role="img" aria-label="Pale diagonal stripe texture in a large curved area with a sweeping white arc band">
      <rect width="475" height="275" fill="var(--card)"/>
      <ellipse cx="180" cy="120" rx="245" ry="245" fill="var(--stripe-pale)"/>
      <path fill="var(--stripe-pale)" d="M475 195 L475 275 L438 275 Q462 240 475 195 Z"/>
    </svg>
    <div class="wordmark">Tallo Ventures</div>
    <div class="contact">
      <p class="contact__business">Business Name</p>
      <p class="contact__name">Name</p>
      <p class="contact__position">Position</p>
      <p class="contact__address">Address line 1<br>Address line 2</p>
      <p class="contact__phones">Telephone 1<span class="sep">•</span>Telephone 2</p>
      <p class="contact__web">Email<span class="sep">•</span>Website</p>
    </div>
  </section>

  <div class="board-rule"></div>
  <div class="board-mark">Tallo Ventures</div>
</body>
</html>
```